Awesome, colorful pamphlet advertising services for disabled people and supporters

My business, The Ability Crossroads, provides nutritional counseling services to people with and without disabilities throughout the lifespan. It also offers disability consulting, body image coaching and accessible recreation consultation. I would like something representing both children and adults which ties these activities together in a happy way.

Font styles to use
Sans Serif

Colors
00AB8E
00BBA5
67D7C9
C6EFE9
E9F9F6
FFF300
FFF600
FEFA6F
FFFEC7
FFFEE8
F0912C
F2A743
F7CA91
FBE8D2
FDF5EE
E54698
E96AAD
F1A4CE
F9D9EA
FCEFF6
6B429C
8869AF
B7A5CE
E3DAEB
F3F0F8

```html
<!DOCTYPE html>
<html lang="en">
<head>
<meta charset="utf-8">
<title>The Ability Crossroads – Trifold Brochure</title>
<link href="https://fonts.googleapis.com/css2?family=Source+Sans+3:ital,wght@0,400;0,600;0,700;1,600&display=swap" rel="stylesheet">
<style>
  :root{
    --bg:#bcbec0;
    --purple:#6B429C;
    --purple-deep:#3d2170;
    --purple-mid:#5a3590;
    --lavender:#b58fc9;
    --lavender-soft:#E3DAEB;
    --gold:#f5c400;
    --gold-soft:#FEFA6F;
    --ink:#555459;
    --white:#ffffff;
    --paper:#f4f4f6;
  }
  *{box-sizing:border-box;margin:0;padding:0}
  html,body{width:910px;height:1200px;overflow:hidden}
  body{background:var(--bg);font-family:"Source Sans 3",Arial,sans-serif;color:var(--ink);position:relative}
  .sheet{position:absolute;left:125px;width:660px;height:510px;display:flex;box-shadow:0 10px 14px -6px rgba(0,0,0,.35)}
  .sheet--outside{top:70px}
  .sheet--inside{top:620px}
  .panel{position:relative;width:220px;height:510px;overflow:hidden}
  .panel--light{background:linear-gradient(180deg,var(--white),var(--paper))}
  .panel--purple{background:linear-gradient(160deg,var(--purple-mid),var(--purple-deep));color:var(--white)}
  .photo{position:absolute;left:0;width:220px}
  .swoosh{position:absolute;left:0;width:220px}
  .h-purple{color:var(--purple);font-weight:600;font-size:13px;line-height:1.1;text-transform:uppercase}
  .h-gold{color:var(--gold);font-weight:600;font-size:13px;line-height:1.2;text-transform:uppercase;text-align:center}
  .body-text{font-size:7.6px;line-height:1.42;text-align:justify}
  .bullets{list-style:none}
  .bullets li{position:relative;padding-left:11px;font-size:7.4px;line-height:1.3;margin-bottom:5px}
  .bullets li::before{content:"";position:absolute;left:0;top:1.5px;width:6px;height:6px;border-radius:50%;background:var(--gold)}
  .bullets li::after{content:"";position:absolute;left:1.2px;top:3.6px;width:2px;height:2px;border-right:1px solid var(--white);border-top:1px solid var(--white);transform:rotate(45deg)}
  .url-pill{position:absolute;bottom:0;left:10px;width:200px;height:22px;border-radius:11px 11px 0 0;background:var(--purple);color:var(--white);font-weight:700;font-size:9px;letter-spacing:.5px;display:flex;align-items:center;justify-content:center}
  .url-pill--soft{background:var(--lavender)}
  .gold-bar{position:absolute;bottom:10px;left:0;width:220px;height:19px;background:var(--gold);color:var(--white);font-weight:700;font-size:9px;letter-spacing:.3px;display:flex;align-items:center;justify-content:center;gap:5px}
  .gold-bar .dot{width:7px;height:7px;border-radius:50%;background:var(--white);opacity:.8}
  .sub-gold{color:var(--gold);font-size:9.5px;text-align:center;line-height:1.2;margin:12px 0 8px}
</style>
</head>
<body>

<!-- Outside of the brochure -->
<section class="sheet sheet--outside">

  <article class="panel panel--light about">
    <div class="photo" role="img" aria-label="Photo of a group of people, one in a wheelchair, holding hands raised in a circle on a grassy field" style="top:0;height:215px;background:linear-gradient(180deg,#9fae6a 0%,#6f8a3e 45%,#4f6a2c 100%)"></div>
    <svg class="swoosh" style="top:180px" width="220" height="60" viewBox="0 0 220 60" aria-hidden="true">
      <path d="M0 22 Q110 -6 220 18 L220 60 L0 60Z" fill="var(--gold)"/>
      <path d="M0 34 Q110 6 220 30 L220 60 L0 60Z" fill="var(--white)"/>
    </svg>
    <div role="img" aria-label="Portrait of Dana Whitford" style="position:absolute;left:128px;top:175px;width:76px;height:76px;border-radius:50%;border:4px solid var(--lavender);background:linear-gradient(160deg,#c9a58a,#8a6650)"></div>
    <div style="position:absolute;left:14px;top:225px;width:196px">
      <h2 class="h-purple">About Dana</h2>
      <p style="color:var(--purple);font-size:7.6px;margin:2px 0 8px">Dana Whitford, MSW, CARSS I,</p>
      <p class="body-text">CFNC has been passionate about disability issues since 2003 when she discovered disability rights and the disability activism community. This changed her life and helped her feel stronger about herself, her disabilities, and her capabilities. She has been working toward being a Certified Body Image Coach.</p>
      <p style="font-size:7.8px;font-weight:600;margin:6px 0 5px">What can a body image coach help you with?</p>
      <ul class="bullets">
        <li>Exploring beliefs about your body and self</li>
        <li>Helping to break down negative messages</li>
        <li>Putting your struggles into a broader context</li>
        <li>Giving you tools to help you in your body</li>
        <li>Help you break free of dieting</li>
        <li>Help you experience greater freedom</li>
      </ul>
      <div style="display:flex;justify-content:center;gap:7px;margin-top:6px">
        <span style="width:28px;height:28px;border-radius:50%;border:2px solid #e54698;background:var(--white)"></span>
        <span style="width:28px;height:28px;border-radius:50%;border:2px solid #b59a8c;background:var(--white)"></span>
        <span style="width:28px;height:28px;border-radius:50%;background:var(--lavender)"></span>
      </div>
    </div>
    <div class="url-pill">www.abilitycrossroads.org</div>
  </article>

  <article class="panel panel--purple welcome">
    <div role="img" aria-label="Photo of a smiling boy in an orange shirt sitting in a wheelchair in a library" style="position:absolute;left:37px;top:38px;width:146px;height:146px;border-radius:50%;border:5px solid var(--lavender);background:linear-gradient(160deg,#b88452,#6a4128)"></div>
    <div style="position:absolute;left:16px;top:196px;width:188px">
      <h1 class="h-gold">Welcome to the<br>Ability Crossroads!</h1>
      <p class="body-text" style="margin-top:10px">I'm Dana, and I hope you find this site informative and helpful. Here you will be able to access material on general disability issues, mental health concerns and trauma intervention as they affect disabled people and members of society at large.</p>
      <p class="body-text" style="margin-top:10px">We are passionate about this. I provide disability aware consultation, writing, speaking and training services to businesses and organizations. Contact me to discuss your needs today!</p>
      <p style="text-align:center;font-size:7.6px;opacity:.75;margin-top:22px">Dana Whitford, MSW, CARSS I,</p>
      <p style="text-align:center;color:var(--gold);font-weight:600;font-size:9px;margin-top:9px">Contact and FREE Appointment</p>
      <div style="display:flex;justify-content:center;gap:12px;margin-top:9px">
        <span style="width:17px;height:17px;border-radius:50%;border:1px solid var(--white)"></span>
        <span style="width:17px;height:17px;border-radius:50%;border:1px solid var(--white)"></span>
        <span style="width:17px;height:17px;border-radius:50%;border:1px solid var(--white)"></span>
      </div>
    </div>
    <div class="url-pill url-pill--soft">www.abilitycrossroads.org</div>
  </article>

  <article class="panel panel--light cover">
    <div class="photo" role="img" aria-label="Photo of four cheerful young children in colorful sweaters making peace signs" style="top:0;height:330px;background:linear-gradient(170deg,#8fa7c4 0%,#c77a86 45%,#d9a05a 100%)"></div>
    <svg class="swoosh" style="top:285px" width="220" height="70" viewBox="0 0 220 70" aria-hidden="true">
      <path d="M0 10 Q120 70 220 14 L220 70 L0 70Z" fill="var(--gold)"/>
      <path d="M0 22 Q120 80 220 30 L220 70 L0 70Z" fill="var(--white)"/>
    </svg>
    <div style="position:absolute;left:0;top:330px;width:220px;text-align:center">
      <div style="width:46px;height:46px;border-radius:50%;border:2px solid var(--lavender-soft);margin:0 auto 6px"></div>
      <p style="color:var(--purple);font-size:10.5px;font-weight:600;text-transform:uppercase">The Ability Crossroads</p>
      <p style="color:var(--purple-deep);font-size:7.8px;font-weight:700;line-height:1.75;margin-top:16px;text-transform:uppercase">Nutritional counseling services<br>to people with and without disabilities<br>throughout the lifespan</p>
    </div>
    <div class="url-pill">www.abilitycrossroads.org</div>
  </article>
</section>

<!-- Inside of the brochure -->
<section class="sheet sheet--inside">

  <article class="panel panel--light classes">
    <div style="position:absolute;left:12px;top:22px;width:196px">
      <h2 class="h-purple">Let's hear it for<br>Songsprout!</h2>
      <p class="body-text" style="margin-top:8px">The Ability Crossroads is launching virtual toddler (16 months-3 and a half years) and preschool age (3-5) Songsprout classes for fall. These will be held over online video. Children of all abilities and their grownups welcome. More information to follow.</p>
      <p class="body-text" style="margin-top:10px">I teach Songsprout because above all, it has a deep respect for child development and is evidence based. It fosters important skills for social and school success, and is a great way to have fun with the child in your life!</p>
      <p class="body-text" style="margin-top:10px">For more information on classes and to enroll a child, please email me at:</p>
      <p style="margin:12px auto 0;width:158px;height:14px;border-radius:7px;background:var(--lavender);color:var(--white);font-size:7.6px;text-align:center;line-height:14px">hello@abilitycrossroads.org</p>
      <p style="font-style:italic;font-weight:600;font-size:7.8px;text-align:center;margin-top:6px">I'm looking forward to hearing from you!</p>
    </div>
    <div class="photo" role="img" aria-label="Photo of three smiling young girls sitting close together" style="top:300px;height:210px;background:linear-gradient(160deg,#8b6a55,#b69d8a 45%,#6f7fa3)"></div>
    <svg class="swoosh" style="top:290px" width="220" height="50" viewBox="0 0 220 50" aria-hidden="true">
      <path d="M0 0 L220 0 L220 8 Q110 -4 0 36Z" fill="var(--white)"/>
      <path d="M0 36 Q110 -4 220 8 L220 14 Q110 4 0 44Z" fill="var(--gold)"/>
    </svg>
  </article>

  <article class="panel panel--purple services">
    <div style="position:absolute;left:10px;top:22px;width:200px">
      <h2 style="text-align:center;font-size:12.5px;font-weight:600">OUR SERVICES</h2>
      <p style="text-align:center;color:var(--gold);font-size:9.5px;margin:2px 0 12px">Individuals/Families/Small Groups</p>
      <ul class="bullets">
        <li>Self and Body esteem as related to disability</li>
        <li>Trauma and healing with a disability</li>
        <li>Early childhood support for disabled children and care providers</li>
      </ul>
      <p class="sub-gold">General disability issues/peer<br>level support</p>
      <ul class="bullets">
        <li>Movement as fun for disabled kids and adults</li>
        <li>Moving away from therapies / assessing therapy from a disability positive perspective</li>
        <li>Accessible Recreation/Play Consults</li>
      </ul>
      <p class="sub-gold" style="margin-top:28px">Services we will proudly offer</p>
      <ul class="bullets">
        <li>CircleChat™ senior socialization groups</li>
        <li>Songsprout early childhood music and movement classes for infants and children up to age 7</li>
        <li>Functional nutrition consultation</li>
        <li>Consultation for people with chronic illnesses such as Postural Orthostatic Tachycardia Syndrome (POTS) and Neurocardiogenic Syncope</li>
      </ul>
      <p class="sub-gold" style="margin-top:10px">Other services</p>
      <ul class="bullets">
        <li>Play Groups</li>
        <li>Classes and social groups for teenagers</li>
        <li>Social groups for veterans</li>
      </ul>
    </div>
    <div class="gold-bar">Contact and FREE Appointment</div>
  </article>

  <article class="panel panel--light meaning">
    <div class="photo" role="img" aria-label="Photo of a smiling couple embracing, the man seated in a wheelchair in a bright home" style="top:0;height:210px;background:linear-gradient(160deg,#e4e0da,#a9b5c6 55%,#7c6a5c)"></div>
    <svg class="swoosh" style="top:175px" width="220" height="60" viewBox="0 0 220 60" aria-hidden="true">
      <path d="M0 26 Q130 36 220 0 L220 60 L0 60Z" fill="var(--gold)"/>
      <path d="M0 34 Q130 44 220 10 L220 60 L0 60Z" fill="var(--white)"/>
    </svg>
    <div style="position:absolute;left:11px;top:240px;width:198px">
      <h2 class="h-purple" style="font-size:11.5px">What these disabilities actually<br>mean may surprise you</h2>
      <p class="body-text" style="margin-top:8px">I am an SLS client. What is SLS? This stands for supported living services, which are personalized supports for people whose disabilities are considered developmental.</p>
      <p class="body-text" style="margin-top:10px">These disabilities include epilepsy in childhood, autism, down syndrome and other chromosome related disabilities, intellectual disabilities, cerebral palsy and in many cases spina bifida.</p>
      <p class="body-text" style="margin-top:10px">Because the definition means neurologically based, it excludes physical disabilities in which motor issues are the result of muscle issues only such as muscular dystrophy, ALS, muscle issues from severe illness, etc.</p>
    </div>
    <div class="gold-bar"><span class="dot"></span>www.abilitycrossroads.org</div>
  </article>
</section>

</body>
</html>
```